Stylish Business Cards Wanted

- DOUBLE SIDED Design Required -

High end, edgy cards for a corporate and personal stylist. Must include logo,
Name: Belinda Forsey
Title: Director and Stylist
telephone : +61 8 8217 4592
email: belinda@thegarbledger.example
website: thegarbledger.example
Tag: Corporate Workwear & Uniform Specialist | Personal Stylist
Would like nice icons for telephone, email, website

Target Market(s)

Businesses wanting stylish uniforms, people wanting stylish wardrobes

Industry/Entity Type

Corporate Workwear Stylist

Contact Information for Business Card

I would like black, white and gold foiling incorporated in the design - possibly a touch of the other colours on my branding guide attached Name: Belinda Forsey Title: Director and Stylist telephone : +61 8 8217 4592 email: belinda@thegarbledger.example website: thegarbledger.example Tag: Corporate Workwear & Uniform Specialist | Personal Stylist Would like nice icons for telephone, email, website

Font styles to use
Other font styles liked:
• Raleway

Colors

Designer to choose colors to be used in the design.

Requirements
Must have
• Gold foil accents

```html
<!DOCTYPE html>
<html lang="en">
<head>
<meta charset="utf-8">
<title>The Garb Ledger – Business Card</title>
<link rel="stylesheet" href="https://fonts.googleapis.com/css2?family=Raleway:wght@400;500;600;700&display=swap">
<style>
  :root {
    --backdrop: #e9e9ea;
    --card: #ffffff;
    --card-edge: #d4d4d4;
    --ink: #1f1d1d;
    --gold: #e0b54b;
    --rule: #6b6b6b;
  }
  * { margin: 0; padding: 0; box-sizing: border-box; }
  html, body {
    width: 1200px;
    height: 507px;
    overflow: hidden;
    background: var(--backdrop);
    font-family: "Raleway", sans-serif;
    color: var(--ink);
  }
  .canvas { position: relative; width: 1200px; height: 507px; }

  .card {
    position: absolute;
    top: 106px;
    width: 493px;
    height: 296px;
    background: var(--card);
    border: 1px solid var(--card-edge);
  }
  .card--front { left: 83px; }
  .card--back  { left: 624px; }

  .wordmark {
    font-family: "Raleway", sans-serif;
    font-weight: 700;
    color: var(--ink);
    white-space: nowrap;
    letter-spacing: 0.01em;
  }

  /* front */
  .front-brand {
    position: absolute;
    left: 53px;
    top: 98px;
    width: 125px;
    height: 88px;
    display: flex;
    align-items: center;
    justify-content: center;
  }
  .front-brand .wordmark { font-size: 16px; }
  .divider {
    position: absolute;
    left: 187px;
    top: 89px;
    width: 1px;
    height: 108px;
    background: var(--rule);
  }
  .contact {
    position: absolute;
    left: 202px;
    top: 87px;
  }
  .contact__name {
    font-weight: 600;
    font-size: 22px;
    line-height: 26px;
    color: var(--gold);
  }
  .contact__title {
    font-size: 11px;
    line-height: 13px;
    margin-bottom: 9px;
  }
  .contact__list { list-style: none; }
  .contact__item {
    display: flex;
    align-items: center;
    font-size: 14.5px;
    line-height: 21.5px;
    white-space: nowrap;
  }
  .contact__icon {
    width: 11px;
    height: 11px;
    margin-right: 6px;
    flex: none;
  }
  .tagline {
    position: absolute;
    left: 55px;
    top: 232px;
    width: 384px;
    height: 26px;
    border: 1px solid var(--ink);
    display: flex;
    align-items: center;
    justify-content: center;
    font-size: 10.6px;
    letter-spacing: -0.01em;
    white-space: nowrap;
    overflow: hidden;
  }
  .tagline__sep { margin: 0 5px; }

  /* back */
  .back-frame {
    position: absolute;
    left: 143px;
    top: 75px;
    width: 206px;
    height: 146px;
    border: 1px solid var(--ink);
    display: flex;
    align-items: center;
    justify-content: center;
  }
  .back-frame .wordmark { font-size: 21px; }
</style>
</head>
<body>
<main class="canvas">

  <section class="card card--front" aria-label="Card front">
    <div class="front-brand"><span class="wordmark">The Garb Ledger</span></div>
    <div class="divider"></div>
    <div class="contact">
      <p class="contact__name">Belinda Forsey</p>
      <p class="contact__title">Director and Stylist</p>
      <ul class="contact__list">
        <li class="contact__item">
          <svg class="contact__icon" viewBox="0 0 12 12" aria-hidden="true">
            <circle cx="6" cy="6" r="6" fill="var(--gold)"/>
            <path d="M3 7.6h6v1.2H3z M3.2 6.8c0-1.8 1.3-2.8 2.8-2.8s2.8 1 2.8 2.8z" fill="#fff"/>
          </svg>
          +61 8 8217 4592
        </li>
        <li class="contact__item">
          <svg class="contact__icon" viewBox="0 0 12 12" aria-hidden="true">
            <circle cx="6" cy="6" r="6" fill="var(--gold)"/>
            <rect x="3" y="4" width="6" height="4.2" fill="#fff"/>
            <path d="M3 4l3 2.3L9 4" fill="none" stroke="var(--gold)" stroke-width="0.7"/>
          </svg>
          belinda@thegarbledger.example
        </li>
        <li class="contact__item">
          <svg class="contact__icon" viewBox="0 0 12 12" aria-hidden="true">
            <circle cx="6" cy="6" r="6" fill="var(--gold)"/>
            <g fill="none" stroke="#fff" stroke-width="0.7">
              <circle cx="6" cy="6" r="3.2"/>
              <ellipse cx="6" cy="6" rx="1.4" ry="3.2"/>
              <path d="M2.8 6h6.4"/>
            </g>
          </svg>
          thegarbledger.example
        </li>
      </ul>
    </div>
    <div class="tagline">
      <span>CORPORATE WORKWEAR</span><span class="tagline__sep">|</span>
      <span>UNIFORM SPECIALIST</span><span class="tagline__sep">|</span>
      <span>PERSONAL STYLIST</span>
    </div>
  </section>

  <section class="card card--back" aria-label="Card back">
    <div class="back-frame"><span class="wordmark">The Garb Ledger</span></div>
  </section>

</main>
</body>
</html>
```